Property lawyer needs a website for new law firm Sydney

WHO AM I ?
I am a real estate development lawyer based in suburban Sydney Australia with over 14 years experience and have recently started my own law firm "Tallowbrook Legal". The firm is just me (a female) at this stage. I need a website designed that is capable of being edited by me frequently (hoping this is easily done?!) and can be published with the domain name I own - www.tallowbrooklegal.com.au.
My areas of practice are:
* Property development (strata & community titling, due diligence, easements, by-laws and management statements, structuring etc)
* Conveyancing (sale and purchase of residential, commercial and retail property)
* General property law (caveats, transfers, related party transactions, easements, leases, powers of attorney etc).
WEBSITE REQUIREMENTS
I would like a website which conveys professionalism, has a fresh modern corporate look and is easy to navigate. The website will mostly be accessed by potential clients looking for information about me, my areas of practice and how to get in contact with me. My potential clients are corporate developers and individuals who are buying and selling property.
My logo for Tallowbrook Legal (see attached) is simple, clean and professional looking. I would like the website to work with the logo without being too dark.
I haven't written all of the content yet, so please use filler text for everything and structure the menus as described above. The site will need to be capable of being updated and edited by me.
Other than that I will leave the design up to you.
Thanks and happy designing!
Target Market(s)
Professional developers and individuals buying and selling real estate
Industry/Entity Type
Real Estate
Coding
Coded - Design and coding required
Number of Pages Required
4 page
Requirements
Must have
- I would like a website which conveys professionalism, has a fresh modern corporate look and is easy to navigate. The website will mostly be accessed by potential clients looking for information about me, my areas of practice and how to get in contact with me. My potential clients are corporate developers and individuals who are buying and selling property.
- Please use my logo for Tallowbrook Legal. I would like the website to work with the logo - the colours are a dark blue (C 100% M 50% B 50%) and grey (C10% B 40%). I don't want the website to be too dark though.
- I am thinking 4 pages. I would like links across the top of the page for "Practice Areas", "About us" and "Contact us" - these should lead to separate landing pages with the content to be inserted later.
- The contact page should contain space for a potential client to send an email enquiry to the following email address "enquiries@tallowbrooklegal.com.au". My contact details are set out in the attached letterhead (see attached).
- I would also like the home page to set out what my three Practice Areas are - Property Development; Conveyancing; General Property Law. Each area should have some filler text under it which will be completed later and a link to be able to take me to the "Practice Areas" page where more detail on each will be provided.
- Please select images that are relevant to my practice as a property lawyer. The photos you use will be the ones which I use so please choose wisely.
- I will need a link on the bottom of the home page showing that I am a member of "The Counsel Guild of NSW" (see attached logo).
- The bottom of each page should also include the following statement "Tallowbrook Legal is a business name of Tallowbrook Legal Pty Limited ACN 482 517 306, an incorporated legal practice regulated by the Legal Profession Act 2004. Liability limited by a scheme approved under the Professional Standards Legislation."
Nice to have
- Have attached an image of me (not the best) but at least its me. Consider whether to use on "About us" page
Should not have
- No images of gavels, scales of justice or law books.
- Images not to be too masculine
- Website not to be too dark

```html
<!DOCTYPE html>
<html lang="en">
<head>
<meta charset="utf-8">
<title>Tallowbrook Legal</title>
<link href="https://fonts.googleapis.com/css2?family=Lato:ital,wght@0,400;0,700;0,900;1,400&family=Roboto+Condensed:wght@700&display=swap" rel="stylesheet">
<style>
:root{
  --navy:#1a4a7d;
  --navy-dark:#0f3a68;
  --bright:#1565b0;
  --grey:#8a97a5;
  --text:#333;
  --light:#f4f4f4;
  --footer:#1e1f22;
}
*{box-sizing:border-box;margin:0;padding:0}
html,body{width:770px;height:1200px;overflow:hidden;background:#fff}
body{position:relative;font-family:'Lato',sans-serif;color:var(--text)}
.abs{position:absolute}
.topbar{left:0;top:0;width:770px;height:22px;background:#f6f6f6;border-bottom:1px solid #e4e4e4}
.social-cell{top:0;width:27px;height:22px;border-left:1px solid #e2e2e2;display:flex;align-items:center;justify-content:center}
.social-cell span{width:8px;height:8px;border-radius:50%;background:#9aa2ab}
.phone-top{left:568px;top:0;width:118px;height:22px;border-left:1px solid #e2e2e2;border-right:1px solid #e2e2e2;font-size:9px;color:#888;display:flex;align-items:center;justify-content:center;gap:5px}
.header{left:0;top:22px;width:770px;height:56px;background:#fff}
.logo{left:84px;top:41px;font-size:16px;font-weight:700;color:var(--navy);letter-spacing:.5px}
.nav-home{left:325px;top:22px;width:48px;height:56px;background:var(--navy);color:#fff;font-size:9px;font-weight:700;display:flex;align-items:center;justify-content:center}
.nav-item{top:49px;font-size:9px;color:#555}
.nav-sep{top:48px;width:1px;height:12px;background:#ccc}
.hero{left:0;top:78px;width:770px;height:304px;
  background:
    radial-gradient(ellipse 170px 150px at 555px 150px,rgba(190,208,228,.75) 0%,rgba(120,150,186,.35) 55%,rgba(0,0,0,0) 100%),
    linear-gradient(180deg,rgba(30,60,100,0) 55%,rgba(45,85,135,.55) 78%,rgba(15,50,95,.8) 100%),
    linear-gradient(90deg,#123a6a 0%,#2d5286 22%,#5677a3 45%,#4d6f9e 70%,#1d4677 100%)}
.hero-title{left:85px;top:202px;width:420px;font-size:20.5px;font-weight:700;color:#fff;line-height:29px}
.btn-outline{left:85px;top:268px;width:83px;height:22px;border:1.5px solid #fff;border-radius:3px;color:#fff;font-size:9.5px;font-weight:700;display:flex;align-items:center;justify-content:center}
.arrow{top:219px;width:30px;height:23px;background:#2c3440;border:1px solid #5a6776;display:flex;align-items:center;justify-content:center}
.section-title{font-size:14px;font-weight:400;color:var(--grey)}
.section-title b{color:var(--navy);font-weight:900}
.pa-title{left:0;width:770px;top:405px;text-align:center}
.pa-rule{left:236px;top:431px;width:298px;height:1px;background:#bbb}
.pa-accent{left:364px;top:430px;width:42px;height:3px;background:var(--navy)}
.card{top:445px;width:188px;height:102px;overflow:hidden}
.card-img{position:absolute;left:0;top:0;width:188px;height:81px}
.card-label{position:absolute;left:0;top:81px;width:188px;height:21px;background:#111;color:#fff;font-family:'Roboto Condensed',sans-serif;font-size:11px;font-weight:700;display:flex;align-items:center;justify-content:center;letter-spacing:.2px}
.divider-shadow{left:0;top:565px;width:770px;height:10px;background:linear-gradient(#f0f0f0,#fff)}
.about-title{left:86px;top:595px}
.about-rule{left:86px;top:617px;width:468px;height:1px;background:#ccc}
.about-text{left:85px;top:628px;width:458px;font-size:8.3px;line-height:11.8px;color:#444}
.about-text p+p{margin-top:4px}
.btn-solid{left:85px;top:706px;width:71px;height:21px;background:var(--navy);color:#fff;font-size:9px;font-weight:700;border-radius:2px;display:flex;align-items:center;justify-content:center}
.portrait{left:565px;top:598px;width:120px;height:129px;border:1px solid #ccc;padding:3px;background:#fff}
.portrait div{width:100%;height:100%;background:radial-gradient(ellipse 40px 50px at 50% 38%,#e7c3ae 0%,#b07a5f 60%,#f2f2f2 100%),#f2f2f2}
.band{left:0;top:758px;width:770px;height:82px;background:var(--navy-dark)}
.badge{left:85px;top:781px;display:flex;align-items:center;gap:6px}
.badge-shield{width:30px;height:34px;background:#fff;opacity:.9;border-radius:3px 3px 15px 15px}
.badge-text{font-size:6px;color:#fff;line-height:7px;width:48px}
.band-text{left:178px;top:782px;width:380px;font-size:11px;font-weight:700;color:#fff;line-height:15.5px}
.btn-contact{left:578px;top:781px;width:108px;height:35px;background:var(--bright);color:#fff;font-size:12px;font-weight:700;border-radius:2px;display:flex;align-items:center;justify-content:center}
.col-title{top:860px}
.col-rule{top:885px;height:1px;background:#ccc}
.col-accent{top:884px;width:44px;height:3px;background:var(--navy)}
.quote{left:85px;top:896px;width:181px;height:102px;background:var(--light);padding:10px 10px 0 12px;font-size:7.6px;font-style:italic;line-height:14.4px;color:#555}
.quote-tip{left:168px;top:997px;width:0;height:0;border-left:8px solid transparent;border-right:8px solid transparent;border-top:8px solid var(--light)}
.avatar{left:153px;top:1015px;width:46px;height:46px;border-radius:50%;border:2px solid #ddd;background:radial-gradient(circle at 50% 40%,#e3b89c 0%,#b98a6c 45%,#dfe6ee 75%)}
.client{left:85px;top:1068px;width:181px;text-align:center;font-size:7.8px;font-weight:700;color:var(--navy)}
.news{left:293px;width:181px}
.news h4{font-size:8.4px;font-weight:700;color:#222}
.news p{font-size:7.8px;line-height:11.8px;color:#555}
.news time{display:block;font-size:7.8px;font-weight:700;color:var(--navy);margin-top:1px;letter-spacing:.3px}
.news-sep{left:293px;width:181px;border-top:1px dashed #bbb}
.vsep{left:279px;top:900px;width:1px;height:170px;background:#eee}
.field{left:503px;width:183px;border:1px solid #c9c9c9;font-size:8px;color:#555;padding:6px 6px}
.btn-submit{left:504px;top:1054px;width:72px;height:21px;background:var(--navy);color:#fff;font-size:8.5px;font-weight:700;border-radius:2px;display:flex;align-items:center;justify-content:center}
.footer{left:0;top:1098px;width:770px;height:102px;background:var(--footer);border-top:2px solid var(--navy-dark)}
.fbox{top:1108px;height:46px;border:1px solid #5d7fa8;background:#1a3c66;color:#fff}
.fbox h5{font-size:9.5px;font-weight:700;margin:3px 0 0 7px}
.fsmall{font-size:7.8px;color:#eee}
.sub-input{position:absolute;left:12px;top:21px;width:116px;height:17px;background:#fff;font-size:7.6px;font-style:italic;color:#555;padding:3px 6px}
.sub-btn{position:absolute;left:132px;top:21px;width:20px;height:17px;background:#8995a3;display:flex;align-items:center;justify-content:center}
.dot{width:17px;height:17px;border-radius:50%;background:#fff;display:inline-block;margin-right:4px}
.flinks{left:85px;top:1161px;font-size:8px;color:#ddd}
.copy{left:463px;top:1161px;width:223px;text-align:right;font-size:8px;color:#ddd}
.legal{left:85px;top:1175px;width:601px;font-size:6.4px;line-height:9px;color:#9a9ea5}
</style>
</head>
<body>

<div class="abs topbar"></div>
<div class="abs social-cell" style="left:86px"><span></span></div>
<div class="abs social-cell" style="left:113px"><span></span></div>
<div class="abs social-cell" style="left:140px"><span></span></div>
<div class="abs social-cell" style="left:167px;border-right:1px solid #e2e2e2"><span></span></div>
<div class="abs phone-top">
  <svg width="9" height="9" viewBox="0 0 10 10"><rect width="10" height="10" rx="2" fill="#9aa2ab"/><path d="M3 2.5c.5 2 2 3.8 4.3 4.8l.7-1-1.3-.7-.6.6C5.3 5.7 4.5 4.9 4 4l.6-.6L3.9 2z" fill="#fff"/></svg>
  +0 155 2468 310
</div>

<div class="abs header"></div>
<div class="abs logo">TALLOWBROOK LEGAL</div>
<div class="abs nav-home">Home</div>
<div class="abs nav-item" style="left:381px">About Us</div>
<div class="abs nav-sep" style="left:437px"></div>
<div class="abs nav-item" style="left:455px">Practice Areas</div>
<div class="abs nav-sep" style="left:532px"></div>
<div class="abs nav-item" style="left:550px">Testimonials</div>
<div class="abs nav-sep" style="left:620px"></div>
<div class="abs nav-item" style="left:638px">Contact Us</div>

<div class="abs hero" role="img" aria-label="Blue-toned photograph of a boardroom table with a brass balance ornament"></div>
<h1 class="abs hero-title">We Are A Pro Real Estate Development Lawyer Based In Suburban Sydney Australia</h1>
<div class="abs btn-outline">Learn More</div>
<div class="abs arrow" style="left:0"><svg width="8" height="10" viewBox="0 0 8 10"><path d="M6 1 2 5l4 4" stroke="#fff" stroke-width="2" fill="none"/></svg></div>
<div class="abs arrow" style="left:740px"><svg width="8" height="10" viewBox="0 0 8 10"><path d="M2 1l4 4-4 4" stroke="#fff" stroke-width="2" fill="none"/></svg></div>

<h2 class="abs section-title pa-title">OUR <b>PRACTICE AREA</b></h2>
<div class="abs pa-rule"></div>
<div class="abs pa-accent"></div>

<div class="abs card" style="left:84px">
  <div class="card-img" role="img" aria-label="Photo of two developers in hard hats viewing a planned building site" style="background:radial-gradient(ellipse 40px 50px at 150px 35px,rgba(40,40,45,.75) 0%,rgba(40,40,45,0) 100%),linear-gradient(180deg,#9fb9d1 0%,#d5e2ec 45%,#b9cfa0 68%,#5f9440 85%,#3f7a2c 100%)"></div>
  <div class="card-label">PROPERTY DEVELOPMENT</div>
</div>
<div class="abs card" style="left:290px">
  <div class="card-img" role="img" aria-label="Photo of hands passing a model house and a set of keys" style="background:radial-gradient(ellipse 35px 30px at 120px 45px,#c3473a 0%,rgba(195,71,58,.4) 55%,rgba(0,0,0,0) 100%),radial-gradient(ellipse 110px 45px at 90px 60px,#e6b49a 0%,#d89c80 50%,rgba(0,0,0,0) 100%),linear-gradient(180deg,#d4d6da 0%,#eeeeee 100%)"></div>
  <div class="card-label">CONVEYANCING</div>
</div>
<div class="abs card" style="left:497px">
  <div class="card-img" role="img" aria-label="Photo of a large two-storey house with a front lawn" style="background:radial-gradient(ellipse 75px 32px at 94px 40px,#f1efe8 0%,#c9c4b4 60%,rgba(0,0,0,0) 100%),linear-gradient(#8db8e3 0%,#c9dced 40%,#8f9a84 68%,#4f7335 85%,#3b5e26 100%)"></div>
  <div class="card-label">GENERAL PROPERTY LAW</div>
</div>

<div class="abs divider-shadow"></div>

<h2 class="abs section-title about-title">ABOUT <b>TALLOWBROOK LEGAL</b></h2>
<div class="abs about-rule"></div>
<div class="abs about-text">
  <p>Lorem ipsum dolor sit amet, consectetur adipiscing elit. Aenean et dignissim sem, interdum risus. Vestibulum consectetur nisi mollis diam pulvinar adipiscing. Vestibulum ut urna nec nibh adipiscing facilisis. Etiam auctor porta lacus ac luctus. Praesent ac libero fermentum, rhoncus magna a, dapibus mauris. Nam ut auctor justo. Sed ante odio, luctus quis nequ nec, adipiscing eleifend arcu. Integer nunc turpis, porttitor at lorem ut.</p>
  <p>Quisque hendrerit molestie commodo. Aliquam imperdiet varius tortor ut condiment Nulla ornare ultricies nunc et scelerisque. Class aptent taciti sociosqu ad litora torquent conubia</p>
</div>
<div class="abs btn-solid">Read More</div>
<div class="abs portrait"><div role="img" aria-label="Portrait photo of the principal lawyer"></div></div>

<div class="abs band"></div>
<div class="abs badge">
  <div class="badge-shield"></div>
  <div class="badge-text">MEMBER OF<br>THE COUNSEL GUILD OF NSW</div>
</div>
<div class="abs band-text">We Are A Pro Real Estate Development Lawyer Based In Suburban Sydney Australia,with Memer Of The Counsel Guild of NSW</div>
<div class="abs btn-contact">Contact Now</div>

<h2 class="abs section-title col-title" style="left:85px">CLIENT <b>TESTIMONIALS</b></h2>
<div class="abs col-rule" style="left:85px;width:181px"></div>
<div class="abs col-accent" style="left:85px"></div>
<div class="abs quote"><span style="font-size:18px;color:#ccc;font-style:normal;line-height:0;vertical-align:-6px">&ldquo;</span> Lorem ipsum dolor consctuer adipiscing elit, sed diam nonm dolor consctuer adipiscing elit, sed diam nonm. Lorem ipsum dolor sit amet, consectet adipiscing elit. Sed quis magna rhoncus, mollis or adipiscing arcu. Suspendisse sagittis orci rutrum, aliqu arcu</div>
<div class="abs quote-tip"></div>
<div class="abs avatar" role="img" aria-label="Client portrait photo"></div>
<div class="abs client">Mr. Quis Nostrud Exerci</div>

<div class="abs vsep"></div>

<h2 class="abs section-title col-title" style="left:293px">LATEST <b>LAW NEWS</b></h2>
<div class="abs col-rule" style="left:293px;width:181px"></div>
<div class="abs col-accent" style="left:293px"></div>
<article class="abs news" style="top:896px"><h4>Lorem ipsum dolor sit amet consctuer</h4><p>Sed diam nonmy nibh eumod tincidunt ut laoreet dolore magna aliquam erat volutpat.</p><time>09/March/2015</time></article>
<div class="abs news-sep" style="top:953px"></div>
<article class="abs news" style="top:962px"><h4>Lorem ipsum dolor sit amet consctuer</h4><p>Sed diam nonmy nibh eumod tincidunt ut laoreet dolore magna aliquam erat volutpat.</p><time>02/March/2015</time></article>
<div class="abs news-sep" style="top:1020px"></div>
<article class="abs news" style="top:1030px"><h4>Lorem ipsum dolor sit amet consctuer</h4><p>Sed diam nonmy nibh eumod tincidunt ut laoreet dolore magna aliquam erat volutpat.</p><time>21/Feb/2015</time></article>

<h2 class="abs section-title col-title" style="left:503px">APPOINTMENT <b>WITH US</b></h2>
<div class="abs col-rule" style="left:503px;width:183px"></div>
<div class="abs col-accent" style="left:503px"></div>
<div class="abs field" style="top:897px;height:21px">Name*</div>
<div class="abs field" style="top:926px;height:21px">Email*</div>
<div class="abs field" style="top:956px;height:21px">Phone*</div>
<div class="abs field" style="top:985px;height:63px">Message*</div>
<div class="abs btn-submit">Submit</div>

<div class="abs footer"></div>
<div class="abs fbox" style="left:85px;width:309px">
  <h5>Contact Us</h5>
  <div class="fsmall" style="position:absolute;left:7px;top:17px;line-height:12px">
    <svg width="7" height="9" viewBox="0 0 7 9" style="vertical-align:-1px"><path d="M3.5 0A3.2 3.2 0 0 0 .3 3.2C.3 5.6 3.5 9 3.5 9s3.2-3.4 3.2-5.8A3.2 3.2 0 0 0 3.5 0z" fill="#fff"/><circle cx="3.5" cy="3.2" r="1.2" fill="#1a3c66"/></svg>
    &nbsp;PO Box 412<br><span style="padding-left:11px">Carlingford NSW 2118</span>
  </div>
  <div style="position:absolute;left:139px;top:16px;width:1px;height:26px;background:#4b6d96"></div>
  <div class="fsmall" style="position:absolute;left:186px;top:17px;line-height:12px">
    <svg width="8" height="8" viewBox="0 0 10 10" style="vertical-align:-1px"><path d="M2 1c.5 3 3 6 7 7l.5-1.8-2-1-1 1C5 5.5 4.5 5 4 4l1-1-1-2z" fill="#fff"/></svg>
    &nbsp;0 455-210-684<br>
    <svg width="8" height="6" viewBox="0 0 8 6" style="vertical-align:0"><rect width="8" height="6" fill="#fff"/><path d="M0 0l4 3 4-3" stroke="#1a3c66" fill="none"/></svg>
    &nbsp;info@tallowbrooklegal.com.au
  </div>
</div>
<div class="abs fbox" style="left:420px;width:164px">
  <h5 style="margin-left:12px">Subscribe to Newsletter</h5>
  <div class="sub-input">Email here</div>
  <div class="sub-btn"><svg width="6" height="8" viewBox="0 0 6 8"><path d="M1 1l3 3-3 3" stroke="#fff" stroke-width="1.6" fill="none"/></svg></div>
</div>
<div class="abs fbox" style="left:610px;width:75px">
  <h5>Follow Us</h5>
  <div style="position:absolute;left:7px;top:21px"><span class="dot"></span><span class="dot"></span><span class="dot"></span></div>
</div>
<div class="abs flinks">Home &nbsp;|&nbsp; Practice Areas &nbsp;|&nbsp; About Us &nbsp;|&nbsp; Testimonials &nbsp;|&nbsp; Contact Us</div>
<div class="abs copy">Copyright &copy; 2015 Tallowbrook Legal. All right reserved.</div>
<p class="abs legal">Tallowbrook Legal is a business name of Tallowbrook Legal Pty Limited ACN 482 517 306, an incorporated legal practice regulated by the Legal Profession Act 2004. Liability limited by a scheme approved under the Professional Standards Legislation.</p>

</body>
</html>
```